Refresh existing website - vlqadm.org

Apply these upgrades to the existing website
1. Modern Design: Update the overall aesthetic to a clean, contemporary look with bold typography,
vibrant colors, and improved visual hierarchy.
2. Mobile Optimization: Enhance responsiveness for seamless navigation on mobile devices.
3. Intuitive User Interface: Simplify navigation by reducing menu complexity and improving call-to-
action buttons.
4. SEO Optimization: Improve content for better ranking on search engines.
5. Accessibility: Ensure compliance with WCAG standards for inclusivity.
6. Faster Load Times: Optimize images and scripts for better performance.
7. Social Media Integration: Add live social media feeds to showcase community engagement.
8. Prefer html

```html
<!DOCTYPE html>
<html lang="en">
<head>
<meta charset="utf-8">
<title>VLQADM – Healthcare Business Consultants</title>
<link href="https://fonts.googleapis.com/css2?family=Roboto:wght@400;500;700;900&display=swap" rel="stylesheet">
<style>
:root{
  --slate:#3d5568;
  --slate-dark:#33495a;
  --green:#6a8c2a;
  --green-light:#86a84a;
  --ink:#333a40;
  --muted:#5b636a;
  --line:#d7dbde;
  --soft:#eef1f3;
  --white:#ffffff;
}
*{box-sizing:border-box;margin:0;padding:0}
html,body{width:1200px;height:5085px;overflow:hidden}
body{position:relative;font-family:"Roboto",Arial,sans-serif;color:var(--ink);background:var(--white)}
.abs{position:absolute}
.btn{position:absolute;display:flex;align-items:center;justify-content:center;background:var(--green);color:var(--white);font-weight:700;font-size:15px;text-transform:uppercase;letter-spacing:.3px;box-shadow:3px 3px 0 rgba(0,0,0,.12)}
.title{font-weight:900;text-transform:uppercase;color:var(--slate);letter-spacing:.5px}
.title em{font-style:normal;color:var(--green)}
.photo{position:absolute}
.bar-hatch{position:absolute;height:24px;background:#d9dcdf}

/* top bar */
.topbar{top:0;left:0;width:1200px;height:43px;background:var(--slate)}
.topbar .mail-side{position:absolute;left:602px;top:0;width:598px;height:43px;background:var(--green)}
.topbar .item{position:absolute;top:0;height:43px;display:flex;align-items:center;gap:10px;color:var(--white);font-size:15px}
/* header */
.header{top:43px;left:0;width:1200px;height:69px;background:var(--white)}
.brand{position:absolute;left:108px;top:12px;width:208px;height:70px;border:2px solid var(--slate);display:flex;align-items:center;justify-content:center;font-weight:900;font-size:40px;color:var(--slate);letter-spacing:1px;background:var(--white)}
.nav{position:absolute;top:0;height:69px;display:flex;align-items:center;font-size:16px;color:var(--ink)}
.nav.active{background:#eef1ea;color:var(--green);padding:0 14px;left:436px}
/* hero */
.hero{top:112px;left:0;width:1200px;height:588px;background:var(--white)}
.hero h1{position:absolute;left:110px;top:113px;font-size:42px;line-height:51px;font-weight:900;color:#1f2429;text-transform:uppercase}
.hero .arrow{position:absolute;top:488px;width:40px;height:40px;border-radius:50%}
/* intro */
.intro{top:700px;left:0;width:1200px;height:570px;background:var(--slate)}
.intro .tag{position:absolute;left:426px;top:93px;width:346px;height:42px;background:#566c7c;color:var(--white);font-size:16px;font-weight:500;display:flex;align-items:center;justify-content:center}
.intro h2{position:absolute;left:0;width:1200px;top:158px;text-align:center;color:var(--white);font-size:38px;font-weight:700}
.intro p{position:absolute;left:195px;width:810px;top:222px;color:var(--white);font-size:13.5px;line-height:25.6px;text-align:justify;text-align-last:center}
/* text blocks */
.copy{position:absolute;font-size:13.5px;line-height:25.6px;color:var(--muted);text-align:justify}
.frame{position:absolute;border:3px solid var(--green);background:var(--white)}
/* services */
.services{top:2501px;left:0;width:1200px;height:801px;background:var(--soft)}
.skyline{position:absolute;left:0;top:620px;width:1200px;height:181px;background:linear-gradient(180deg,rgba(238,241,243,0) 0%,#b8c4cd 55%,#8fa1ae 100%)}
.card{position:absolute;top:175px;height:394px;border:3px solid var(--green);background:var(--white)}
.card .pic{position:absolute;left:20px;top:24px;right:20px;height:290px}
.card .name{position:absolute;left:0;right:0;top:330px;text-align:center;font-weight:700;font-size:16px;line-height:24px;color:#222}
.slider-arrow{position:absolute;width:40px;height:40px;border-radius:50%;background:var(--green)}
/* dentists */
.dentist{position:absolute;top:3474px;width:245px;height:318px}
.profile{position:absolute;left:27px;top:28px;width:195px;height:264px;background:var(--white);text-align:center;padding-top:32px}
/* vendors */
.vendor{position:absolute;top:4068px;width:138px;height:138px;border-radius:50%;background:var(--white);box-shadow:0 4px 16px rgba(0,0,0,.1);display:flex;align-items:center;justify-content:center;font-size:22px;color:#444;font-weight:500}
/* contact */
.footer{top:4476px;left:0;width:1200px;height:609px;background:var(--slate)}
.contact-box{position:absolute;left:596px;top:4311px;width:454px;height:404px;background:var(--green);color:var(--white)}
.contact-row{position:absolute;left:60px;display:flex;align-items:center;gap:22px;font-size:20px;font-weight:500;line-height:26px}
.contact-row .ico{width:44px;height:44px;border-radius:50%;background:rgba(255,255,255,.22);display:flex;align-items:center;justify-content:center;flex:none}
.foot-links{position:absolute;left:0;width:1200px;text-align:center;color:var(--white);font-size:14.5px}
.foot-links span{margin:0 12px}
.social{position:absolute;top:4990px;width:34px;height:34px;border-radius:50%;border:2px solid var(--white)}
</style>
</head>
<body>

<!-- top bar -->
<div class="abs topbar">
  <div class="mail-side"></div>
  <div class="item" style="left:110px">
    <svg width="15" height="15" viewBox="0 0 24 24"><path fill="#fff" d="M6.6 10.8a15 15 0 0 0 6.6 6.6l2.2-2.2a1 1 0 0 1 1-.25 11.4 11.4 0 0 0 3.6.57 1 1 0 0 1 1 1V20a1 1 0 0 1-1 1A17 17 0 0 1 3 4a1 1 0 0 1 1-1h3.5a1 1 0 0 1 1 1c0 1.25.2 2.45.57 3.57a1 1 0 0 1-.25 1z"/></svg>
    <span>Phone : <b>571-555-0198</b></span>
  </div>
  <div class="item" style="right:110px">
    <svg width="16" height="13" viewBox="0 0 24 18"><path fill="#fff" d="M0 0h24v2L12 10 0 2zM0 5l12 8 12-8v13H0z"/></svg>
    <span>Email : <b>info@vlqadm.org</b></span>
  </div>
</div>

<!-- header -->
<header class="abs header">
  <div class="brand">VLQADM</div>
  <div class="nav active" style="width:60px;justify-content:center">Home</div>
  <div class="nav" style="left:531px">About</div>
  <div class="nav" style="left:610px">Membership</div>
  <div class="nav" style="left:740px">Services</div>
  <div class="nav" style="left:838px">Upcoming Education</div>
  <div class="nav" style="left:1030px">More
    <svg width="10" height="6" viewBox="0 0 10 6" style="margin-left:6px"><path fill="#6a8c2a" d="M0 0h10L5 6z"/></svg>
  </div>
</header>

<!-- hero -->
<section class="abs hero">
  <svg class="abs" style="left:405px;top:0" width="795" height="588" viewBox="0 0 795 588">
    <polygon points="230,0 260,0 100,588 70,588" fill="#6a8c2a"/>
  </svg>
  <div class="photo" role="img" aria-label="Three smiling doctors in white coats looking at a tablet" style="left:430px;top:0;width:770px;height:588px;background:linear-gradient(120deg,#dfe4e8 0%,#c9cfd4 40%,#8d99a3 100%);clip-path:polygon(170px 0,770px 0,770px 588px,0 588px)"></div>
  <h1>We are the<br>professionals<br>in the business<br>of healthcare</h1>
  <div class="btn" style="left:110px;top:332px;width:251px;height:46px">Join VLQADM Today!</div>
  <div class="arrow" style="left:110px;background:#e7e9eb">
    <svg width="40" height="40" viewBox="0 0 40 40"><path d="M23 13l-7 7 7 7" stroke="#555" stroke-width="2" fill="none"/></svg>
  </div>
  <div class="arrow" style="left:153px;background:var(--green)">
    <svg width="40" height="40" viewBox="0 0 40 40"><path d="M17 13l7 7-7 7" stroke="#fff" stroke-width="2.4" fill="none"/></svg>
  </div>
</section>

<!-- intro -->
<section class="abs intro">
  <div class="tag">VALLEY LEAGUE OF QUALIFIED</div>
  <h2>HEALTHCARE BUSINESS CONSULTANTS</h2>
  <p>For nearly 30 years, the Valley League of Qualified Administrative Managers (VLQADM) and its originating organizations have provided an active forum for networking and knowledge sharing. VLQADM provides members with an in-depth understanding of the constantly changing healthcare business environment – both medical and dental – that is unavailable anywhere else. At our core is the belief that knowledge is gained via continuous professional development, which grows exponentially when we share it with our fellow members through the exchange of insights and best practices. In turn, this helps deliver unparalleled benefits to our members and their clients.</p>
  <div class="btn" style="left:424px;top:397px;width:352px;height:44px;font-size:16px">Upcoming Education Events</div>
</section>

<!-- about -->
<section>
  <div class="bar-hatch" style="left:134px;top:1348px;width:344px"></div>
  <div class="frame" style="left:108px;top:1378px;width:449px;height:442px"></div>
  <div class="photo" role="img" aria-label="Doctor and colleague reviewing documents together" style="left:134px;top:1403px;width:395px;height:393px;background:linear-gradient(160deg,#cfd6dc,#6f7f8c)"></div>
  <div class="bar-hatch" style="left:187px;top:1828px;width:342px"></div>
  <svg class="abs" style="left:59px;top:1542px" width="118" height="118" viewBox="0 0 118 118" aria-label="Play video">
    <circle cx="59" cy="59" r="59" fill="#6a8c2a"/>
    <circle cx="59" cy="59" r="38" fill="#fff"/>
    <path d="M52 46l20 13-20 13z" fill="#6a8c2a"/>
  </svg>
  <h2 class="title abs" style="left:604px;top:1370px;font-size:50px">About <em>VLQADM</em></h2>
  <p class="copy" style="left:604px;top:1444px;width:486px">The Valley League of Qualified Administrative Managers (VLQADM) was founded July 1st, 2006. Its history began when members of the Institute of Practice Management Advisors, the Regional Association of Clinic Advisors, and the Guild of Medical and Dental Practice Managers came together to form one society to best serve practices across all fields.</p>
  <p class="copy" style="left:604px;top:1624px;width:486px">The goal of the VLQADM is the creation of a strong united organization formed from the memberships of the three prior groups. VLQADM combines the talents, skills, and knowledge of these three separate groups to form a society that can better serve the healthcare community as a whole. We aim to provide invaluable resources, education</p>
  <div class="btn" style="left:604px;top:1772px;width:164px;height:46px;font-size:14px">Read More</div>
</section>

<!-- certification -->
<section>
  <h2 class="title abs" style="left:108px;top:1942px;font-size:50px">Our <em>Certification</em></h2>
  <div class="abs" style="left:108px;top:2022px;font-size:16px;font-weight:700;color:var(--slate)">Get Certified as a Healthcare Business Consultant!</div>
  <p class="copy" style="left:110px;top:2058px;width:486px">The CQAM designation shows potential clients, suppliers, and others that the holder has met certain standards of experience and healthcare consulting industry knowledge.</p>
  <p class="copy" style="left:110px;top:2161px;width:486px">This knowledge and experience is outlined in the VLQADM certification Core Body of Knowledge</p>
  <ul class="abs" style="left:110px;top:2222px;width:420px;list-style:none;font-size:13.5px;line-height:25.6px;color:var(--muted)">
    <li style="display:flex;gap:12px"><svg width="14" height="14" viewBox="0 0 14 14" style="margin-top:6px;flex:none"><circle cx="7" cy="7" r="7" fill="#6a8c2a"/><path d="M4 7l2 2 4-4" stroke="#fff" stroke-width="1.6" fill="none"/></svg>Certification Frequency Asked Questions</li>
    <li style="display:flex;gap:12px"><svg width="14" height="14" viewBox="0 0 14 14" style="margin-top:6px;flex:none"><circle cx="7" cy="7" r="7" fill="#6a8c2a"/><path d="M4 7l2 2 4-4" stroke="#fff" stroke-width="1.6" fill="none"/></svg>Membership is the first step</li>
    <li style="display:flex;gap:12px"><svg width="14" height="14" viewBox="0 0 14 14" style="margin-top:6px;flex:none"><circle cx="7" cy="7" r="7" fill="#6a8c2a"/><path d="M4 7l2 2 4-4" stroke="#fff" stroke-width="1.6" fill="none"/></svg>There are three professional designations available<br>through VLQADM:</li>
  </ul>
  <div class="btn" style="left:110px;top:2345px;width:166px;height:44px;font-size:14px">Read More</div>
  <div class="bar-hatch" style="left:720px;top:1915px;width:342px"></div>
  <div class="frame" style="left:643px;top:1946px;width:447px;height:444px"></div>
  <div class="photo" role="img" aria-label="Group of healthcare consultants and doctors reviewing a tablet" style="left:669px;top:1972px;width:395px;height:393px;background:linear-gradient(150deg,#d3dade,#7a8793)"></div>
  <div class="bar-hatch" style="left:669px;top:2397px;width:342px"></div>
</section>

<!-- services -->
<section class="abs services">
  <div class="skyline" role="img" aria-label="Hazy city skyline"></div>
  <h2 class="title abs" style="left:0;width:1200px;text-align:center;top:84px;font-size:50px">Our <em>Services</em></h2>
  <div class="card" style="left:108px;width:308px">
    <div class="pic" role="img" aria-label="Doctor and colleague reviewing a tablet" style="background:linear-gradient(160deg,#e2e6e9,#98a4ad)"></div>
    <div class="name">Payer Quarterly Updates<br>Webinars</div>
  </div>
  <div class="card" style="left:448px;width:304px;height:409px;border:none;background:linear-gradient(180deg,var(--green) 0%,var(--slate) 100%)">
    <div class="pic" role="img" aria-label="Physician and patient looking at a clipboard" style="background:linear-gradient(160deg,#dfe3e6,#8c98a2)"></div>
    <div class="name" style="color:var(--white);top:344px">VLQADM Video Catalog</div>
  </div>
  <div class="btn" style="left:518px;top:2949px;margin-top:-2501px;width:164px;height:44px;font-size:14px">Read More</div>
  <div class="card" style="left:784px;width:308px">
    <div class="pic" role="img" aria-label="Team of medical staff smiling together" style="background:linear-gradient(160deg,#e4e7ea,#93a0aa)"></div>
    <div class="name">VLQADM Practice Benchmarks<br>Reports</div>
  </div>
  <div class="slider-arrow" style="left:36px;top:301px"><svg width="40" height="40" viewBox="0 0 40 40"><path d="M23 13l-7 7 7 7" stroke="#fff" stroke-width="2.4" fill="none"/></svg></div>
  <div class="slider-arrow" style="left:1123px;top:301px"><svg width="40" height="40" viewBox="0 0 40 40"><path d="M17 13l7 7-7 7" stroke="#fff" stroke-width="2.4" fill="none"/></svg></div>
</section>

<!-- dentists -->
<section>
  <h2 class="title abs" style="left:0;width:1200px;text-align:center;top:3390px;font-size:50px">Our <em>Dentists</em></h2>
  <div class="dentist photo" role="img" aria-label="Portrait of a dentist in a white coat" style="left:108px;background:linear-gradient(180deg,#eceeef,#c5cbd0)"></div>
  <div class="dentist" style="left:353px;background:var(--green)">
    <div class="profile">
      <div style="font-size:20px;font-weight:700;color:#222">Dr. Alan Reyes</div>
      <div style="font-size:13.5px;color:var(--green);margin-top:6px">Special Dentist</div>
      <div style="font-size:13.5px;line-height:22px;color:var(--muted);margin:8px 16px 0">Lorem ipsum dolor sit amet, consectetur adipiscing elit, sed do eiusmod tempor</div>
      <div style="width:32px;height:32px;border-radius:50%;background:var(--green);margin:14px auto 0"></div>
    </div>
  </div>
  <div class="dentist photo" role="img" aria-label="Portrait of a dentist wearing gloves" style="left:598px;background:linear-gradient(180deg,#eceeef,#bcc4ca)"></div>
  <div class="dentist photo" role="img" aria-label="Portrait of a dentist with a stethoscope" style="left:843px;background:linear-gradient(180deg,#eceeef,#c2c9ce)"></div>
  <div class="btn" style="left:499px;top:3819px;width:200px;height:46px;font-size:14px">View More Dentists</div>
</section>

<!-- vendors -->
<section>
  <h2 class="title abs" style="left:0;width:1200px;text-align:center;top:3982px;font-size:50px">Sponsoring <em>Vendors</em></h2>
  <svg class="abs" style="left:44px;top:4125px" width="20" height="24" viewBox="0 0 20 24"><path d="M14 3l-9 9 9 9" stroke="#333" stroke-width="2.4" fill="none"/></svg>
  <div class="vendor" style="left:138px">Northline</div>
  <div class="vendor" style="left:336px;font-size:17px">Tessera</div>
  <div class="vendor" style="left:524px;top:4060px;width:152px;height:152px;border:6px solid var(--green);font-size:18px">Caduna</div>
  <div class="vendor" style="left:726px;font-size:18px">Orvia</div>
  <div class="vendor" style="left:922px;font-size:17px">Clearchart</div>
  <svg class="abs" style="left:1134px;top:4125px" width="20" height="24" viewBox="0 0 20 24"><path d="M6 3l9 9-9 9" stroke="#333" stroke-width="2.4" fill="none"/></svg>
</section>

<!-- footer & contact -->
<footer class="abs footer"></footer>
<div class="photo" role="img" aria-label="Street map showing the office location" style="left:144px;top:4311px;width:452px;height:404px;background:linear-gradient(135deg,#eef0f1,#d9dee2)"></div>
<div class="abs" style="left:180px;top:4332px;width:230px;height:64px;background:var(--white);box-shadow:0 2px 8px rgba(0,0,0,.12);font-size:13px;line-height:22px;color:#444;padding:10px 0 0 54px">
  <svg class="abs" style="left:20px;top:18px" width="16" height="22" viewBox="0 0 16 22"><path fill="#6a8c2a" d="M8 0a8 8 0 0 1 8 8c0 6-8 14-8 14S0 14 0 8a8 8 0 0 1 8-8zm0 5a3 3 0 1 0 0 6 3 3 0 0 0 0-6z"/></svg>
  2480 Meridian Park Dr.<br>#310 Fairview, VA 20150
</div>
<div class="contact-box">
  <div class="abs" style="left:66px;top:56px;font-size:38px;font-weight:700">CONTACT US</div>
  <div class="contact-row" style="top:138px">
    <span class="ico"><svg width="16" height="16" viewBox="0 0 24 24"><path fill="#fff" d="M6.6 10.8a15 15 0 0 0 6.6 6.6l2.2-2.2a1 1 0 0 1 1-.25 11.4 11.4 0 0 0 3.6.57 1 1 0 0 1 1 1V20a1 1 0 0 1-1 1A17 17 0 0 1 3 4a1 1 0 0 1 1-1h3.5a1 1 0 0 1 1 1c0 1.25.2 2.45.57 3.57a1 1 0 0 1-.25 1z"/></svg></span>
    Phone: 571-555-0198
  </div>
  <div class="contact-row" style="top:220px">
    <span class="ico"><svg width="14" height="19" viewBox="0 0 16 22"><path fill="#fff" d="M8 0a8 8 0 0 1 8 8c0 6-8 14-8 14S0 14 0 8a8 8 0 0 1 8-8zm0 5a3 3 0 1 0 0 6 3 3 0 0 0 0-6z"/></svg></span>
    <span>2480 Meridian Park Dr.<br>#310 Fairview, VA 20150</span>
  </div>
  <div class="contact-row" style="top:313px">
    <span class="ico"><svg width="16" height="12" viewBox="0 0 24 18"><path fill="#fff" d="M0 0h24v2L12 10 0 2zM0 5l12 8 12-8v13H0z"/></svg></span>
    info@vlqadm.org
  </div>
</div>

<div class="abs" style="left:504px;top:4747px;width:192px;height:62px;border:2px solid var(--white);display:flex;align-items:center;justify-content:center;color:var(--white);font-weight:900;font-size:36px;letter-spacing:1px">VLQADM</div>
<div class="foot-links" style="top:4830px">About the Society<span>/</span>About Membership<span>/</span>Products/ Services<span>/</span>Upcoming Education<span>/</span></div>
<div class="foot-links" style="top:4865px">Practice Reports<span>/</span>Foundation (FQAM)<span>/</span>VLQADM Sponsors<span>/</span>Contact Us</div>
<div class="foot-links" style="top:4945px;font-size:13.5px">© Copyrights 2024 | All Rights Reserved</div>
<div class="social" style="left:524px" aria-label="Social link"></div>
<div class="social" style="left:563px;background:var(--green);border-color:var(--green)" aria-label="Social link"></div>
<div class="social" style="left:603px" aria-label="Social link"></div>
<div class="social" style="left:642px" aria-label="Social link"></div>

</body>
</html>
```